Artist Corinne Beth Marlowe EP Cover

I need this picture used as the cover for my EP Titled Quietly Under Glass... Artist name Corinne Beth Marlowe. Size 1600 X 1600 . I'm attaching the original pic just in case you need that to work from and the one I color enhanced because I think I prefer to use the one with the color enhancements as I think it fits the mood better. But I am open to your creativity and special effects with this photo. Also , here is a previous release I did myself, the idea was to match the fonts on all releases but I am open as long as it doesn't veer away too much. I may possibly need to do the back and inside of case if I print out any Cd's as Well. After front is confirmed then we can work on that. I would like to keep as much as the whole photo in especially the top of the head, if anything is cut off prefer the bottom of the photo:-) Song is moody , maybe in the realm of Altern pop ...ThX

Target Market(s)

Hip , young, cutting edge , pop music fans

Font styles to use
Serif
Sans Serif

Colors
33b8a4
33a6d7
85abd2
876aae

Requirements
Nice to have
• I prefer my name Corinne Beth Marlowe to be in capital letters as it will fit with other releases , but ... I will still look at others if great

```html
<!DOCTYPE html>
<html lang="en">
<head>
<meta charset="utf-8">
<title>Quietly Under Glass – Corinne Beth Marlowe</title>
<link rel="stylesheet" href="https://fonts.googleapis.com/css2?family=Monsieur+La+Doulaise&family=Pathway+Gothic+One&display=swap">
<style>
  :root {
    --cover-night: #0b0c24;
    --cover-deep: #131a45;
    --photo-teal: #2fd9c0;
    --photo-blue: #2a3f9e;
    --photo-indigo: #1b2160;
    --type-violet: #5b55c9;
  }
  html, body {
    margin: 0;
    padding: 0;
    width: 1200px;
    height: 1200px;
    overflow: hidden;
    background: var(--cover-night);
  }
  .ep-cover {
    position: relative;
    width: 1200px;
    height: 1200px;
    overflow: hidden;
    background: linear-gradient(160deg, var(--cover-night) 0%, #0d0f2e 60%, var(--cover-deep) 100%);
  }
  .cover-photo {
    position: absolute;
    left: 380px;
    top: 0;
    width: 820px;
    height: 1200px;
    background:
      radial-gradient(ellipse 200px 260px at 390px 470px, rgba(47, 217, 192, 0.85), rgba(47, 217, 192, 0) 75%),
      radial-gradient(ellipse 300px 420px at 380px 1000px, rgba(47, 217, 192, 0.45), rgba(47, 217, 192, 0) 75%),
      radial-gradient(ellipse 380px 700px at 420px 620px, var(--photo-indigo), rgba(27, 33, 96, 0) 80%),
      linear-gradient(90deg, rgba(11, 12, 36, 0) 0%, rgba(19, 26, 69, 0.6) 40%, var(--photo-blue) 100%);
  }
  .ep-title {
    position: absolute;
    left: 100px;
    top: 120px;
    margin: 0;
    font-family: "Monsieur La Doulaise", cursive;
    font-weight: 400;
    font-size: 150px;
    line-height: 150px;
    color: var(--type-violet);
    transform: rotate(-8deg);
    transform-origin: left top;
  }
  .ep-title span { display: block; }
  .ep-title .line-two { margin-left: 4px; }
  .ep-title .line-three { margin-left: 8px; }
  .artist-name {
    position: absolute;
    left: 48px;
    top: 1113px;
    margin: 0;
    font-family: "Pathway Gothic One", sans-serif;
    font-size: 38px;
    letter-spacing: 0.5px;
    color: var(--type-violet);
    text-transform: uppercase;
  }
</style>
</head>
<body>
  <main class="ep-cover">
    <div class="cover-photo" role="img" aria-label="Portrait of the artist in teal and blue light, wearing a sequinned top, hand resting near her shoulder"></div>
    <h1 class="ep-title">
      <span class="line-one">Quietly</span>
      <span class="line-two">Under</span>
      <span class="line-three">Glass...</span>
    </h1>
    <p class="artist-name">Corinne Beth Marlowe</p>
  </main>
</body>
</html>
```